Granite, Brass and Shingle Roofing LLC needs a new business card

I need a new business card because I have a new address.
I do slate copper and tile roofs. My webpage is: www.granitebrassandshingleroofing.com

```html
<!DOCTYPE html>
<html lang="en">
<head>
<meta charset="utf-8">
<title>Granite, Brass and Shingle Roofing LLC – Business Card</title>
<link rel="stylesheet" href="https://fonts.googleapis.com/css2?family=Poppins:wght@400;500;600&display=swap">
<style>
  :root {
    --page-bg: #d6d4d2;
    --card-dark: #252526;
    --card-blue: #5198c8;
    --card-blue-deep: #4a8bbd;
    --art-blue-light: #5a9fcd;
    --art-blue-dark: #3f7fae;
    --text-light: #f2f2f2;
    --text-dark: #141414;
    --partner-blue: #2a63b8;
    --badge-grey: #bdbdbd;
  }
  html, body {
    margin: 0;
    width: 1200px;
    height: 1200px;
    overflow: hidden;
    background: var(--page-bg);
    font-family: "Poppins", sans-serif;
  }
  .business-card {
    position: absolute;
    left: 60px;
    top: 291px;
    width: 1080px;
    height: 617px;
    background: var(--card-dark);
    overflow: hidden;
  }
  .brand-band {
    position: absolute;
    left: 0;
    right: 0;
    top: 381px;
    bottom: 0;
    background: linear-gradient(90deg, var(--card-blue), var(--card-blue-deep));
  }
  .roof-artwork {
    position: absolute;
    left: 0;
    top: 240px;
    width: 340px;
    height: 377px;
    background: linear-gradient(180deg, var(--art-blue-light), var(--art-blue-dark));
  }
  .partner-badge {
    position: absolute;
    left: 54px;
    top: 47px;
    width: 84px;
    height: 84px;
    border-radius: 50%;
    background: var(--badge-grey);
  }
  .partner-name {
    position: absolute;
    left: 173px;
    top: 70px;
    font-weight: 600;
    font-size: 30px;
    line-height: 1;
    color: var(--partner-blue);
  }
  .owner-block {
    position: absolute;
    right: 39px;
    top: 34px;
    text-align: right;
    color: var(--text-light);
  }
  .owner-name {
    font-weight: 500;
    font-size: 34px;
    line-height: 1.1;
    margin: 0;
  }
  .owner-title {
    font-weight: 400;
    font-size: 25px;
    line-height: 1.3;
    margin: 0;
  }
  .owner-rule {
    position: absolute;
    right: 39px;
    top: 129px;
    width: 66px;
    height: 4px;
    background: var(--text-light);
  }
  .address {
    position: absolute;
    right: 39px;
    top: 168px;
    margin: 0;
    text-align: right;
    font-style: normal;
    font-weight: 500;
    font-size: 28px;
    line-height: 36px;
    color: var(--text-light);
  }
  .online-links {
    position: absolute;
    right: 39px;
    top: 280px;
    text-align: right;
    color: var(--text-light);
    font-size: 25px;
    line-height: 41px;
  }
  .online-links .link-row {
    display: flex;
    justify-content: flex-end;
    align-items: center;
    gap: 9px;
    white-space: nowrap;
  }
  .online-links svg { width: 24px; height: 24px; flex: none; }
  .company-name {
    position: absolute;
    left: 178px;
    top: 488px;
    margin: 0;
    font-weight: 500;
    font-size: 30px;
    line-height: 38px;
    color: var(--text-dark);
  }
  .phone {
    position: absolute;
    right: 39px;
    top: 453px;
    display: flex;
    align-items: center;
    gap: 18px;
    font-weight: 600;
    font-size: 31px;
    color: var(--text-dark);
  }
  .phone svg { width: 34px; height: 34px; }
</style>
</head>
<body>
  <main class="business-card">
    <div class="brand-band"></div>
    <div class="roof-artwork" role="img" aria-label="Illustration of a house roof with chimney and a roofer at work"></div>

    <div class="partner-badge" aria-label="Partner certification badge"></div>
    <div class="partner-name">Apex Membrane</div>

    <div class="owner-block">
      <p class="owner-name">Laszlo (Leo) Varga</p>
      <p class="owner-title">Owner</p>
    </div>
    <div class="owner-rule"></div>

    <address class="address">2871 Millbrook Rd,<br>Millbrook, OH 44390</address>

    <div class="online-links">
      <div class="link-row">www.granitebrassandshingleroofing.com
        <svg viewBox="0 0 24 24" aria-hidden="true"><circle cx="12" cy="12" r="10" fill="none" stroke="currentColor" stroke-width="2"/><ellipse cx="12" cy="12" rx="4" ry="10" fill="none" stroke="currentColor" stroke-width="2"/><line x1="2" y1="12" x2="22" y2="12" stroke="currentColor" stroke-width="2"/></svg>
      </div>
      <div class="link-row">gbsroofingllc@mailbox.com
        <svg viewBox="0 0 24 24" aria-hidden="true"><rect x="2" y="5" width="20" height="14" rx="1" fill="currentColor"/><polyline points="3,6 12,13 21,6" fill="none" stroke="var(--card-dark)" stroke-width="2"/></svg>
      </div>
    </div>

    <p class="company-name">Granite, Brass and Shingle<br>Roofing LLC</p>

    <div class="phone">
      <svg viewBox="0 0 24 24" aria-hidden="true"><path fill="currentColor" d="M6.6 10.8a15.1 15.1 0 0 0 6.6 6.6l2.2-2.2a1 1 0 0 1 1-.25 11.4 11.4 0 0 0 3.6.57 1 1 0 0 1 1 1V20a1 1 0 0 1-1 1A17 17 0 0 1 3 4a1 1 0 0 1 1-1h3.5a1 1 0 0 1 1 1c0 1.25.2 2.45.57 3.57a1 1 0 0 1-.25 1z"/></svg>
      (440) 555 0187
    </div>
  </main>
</body>
</html>
```